Business Card for Auto Dealership - Clean, sharp and professional

Please use the maroon logo with the grey background. Need a sharp, clean and professional business card for an Auto Dealer. In the files provides there is three different logos. I have not decided which one to go with yet. Right now I am favoring the grey/silver background. I would like my contact info on there and the website as well. I feel like less is more and want something simple, clean and sharp. Thank you in advance for your tie and effort! I also need email signature, letterhead, etc after this

Target Market(s)

Car buyers

Industry/Entity Type

Automotive

Contact Information for Business Card

Dean
555-417-2386
www.BrinwoodAutoHub.example
Dean@BrinwoodAutoHub.example

Font styles to use
Serif
Sans Serif

Requirements
Must have
• Please use the maroon logo with the grey background. Business Card Details and logo from files. Please stick to the logo colors

```html
<!DOCTYPE html>
<html lang="en">
<head>
<meta charset="utf-8">
<title>Brinwood Auto Hub – Business Card</title>
<link rel="stylesheet" href="https://fonts.googleapis.com/css2?family=Arimo:wght@400;700&display=swap">
<style>
  :root {
    --maroon: #6e0f12;
    --maroon-deep: #4f0a0c;
    --ink: #1e1e1e;
    --text: #2b2b2b;
    --paper: #f6f6f6;
    --backdrop: #2b2b2b;
    --white: #ffffff;
    --faint: #b9a3a3;
  }
  * { box-sizing: border-box; margin: 0; padding: 0; }
  html, body {
    width: 1200px; height: 997px; overflow: hidden;
    background: var(--backdrop);
    font-family: "Arimo", Arial, sans-serif;
  }
  .stage { position: relative; width: 1200px; height: 997px; }
  .card {
    position: absolute; top: 344px; width: 540px; height: 309px;
    box-shadow: 0 14px 30px rgba(0,0,0,.55);
    overflow: hidden;
  }
  /* Card back */
  .card-back {
    left: 40px;
    background: radial-gradient(ellipse at 55% 40%, #7d1417 0%, var(--maroon) 45%, var(--maroon-deep) 100%);
    display: flex; align-items: center; justify-content: center; gap: 16px;
  }
  .card-back .brand-dot {
    width: 58px; height: 58px; border-radius: 50%; border: 5px solid var(--white);
  }
  .card-back .brand-name {
    color: var(--white); font-weight: 700; font-size: 34px; letter-spacing: 1px;
  }
  /* Card front */
  .card-front { left: 620px; background: var(--paper); }
  .card-front .shapes { position: absolute; inset: 0; }
  .front-brand {
    position: absolute; left: 150px; top: 34px;
    display: flex; align-items: center; gap: 12px;
  }
  .front-brand .brand-dot {
    width: 40px; height: 40px; border-radius: 50%; border: 4px solid var(--maroon);
  }
  .front-brand .brand-name {
    color: var(--maroon); font-weight: 700; font-size: 24px; letter-spacing: .5px;
  }
  .person { position: absolute; left: 24px; top: 118px; }
  .person-name {
    color: var(--maroon); font-weight: 700; font-size: 15px; letter-spacing: .5px;
  }
  .person-role { color: var(--text); font-size: 13px; margin-top: 3px; }
  .contact-list { position: absolute; left: 24px; top: 178px; list-style: none; }
  .contact-list li {
    display: flex; align-items: flex-start; gap: 9px;
    color: var(--text); font-size: 13.5px; line-height: 16px; margin-bottom: 8px;
  }
  .contact-list svg { flex: none; width: 15px; height: 15px; margin-top: 1px; }
  .website {
    position: absolute; right: 20px; bottom: 20px;
    color: var(--white); font-weight: 700; font-size: 13px; white-space: nowrap;
  }
</style>
</head>
<body>
<main class="stage">

  <section class="card card-back" aria-label="Card back">
    <span class="brand-dot"></span>
    <span class="brand-name">BRINWOOD AUTO HUB</span>
  </section>

  <section class="card card-front" aria-label="Card front">
    <svg class="shapes" width="540" height="309" viewBox="0 0 540 309">
      <line x1="150" y1="88" x2="516" y2="88" stroke="var(--maroon)" stroke-width="1.5"/>
      <line x1="146" y1="128" x2="516" y2="128" stroke="var(--maroon)" stroke-width="1.5"/>
      <circle cx="470" cy="196" r="36" fill="none" stroke="var(--faint)" stroke-width="9" opacity=".6"/>
      <path d="M0 284 L250 280 C258 280 260 276 262 272 L264 266 L252 272 C248 274 244 276 238 276 L0 280 Z" fill="var(--ink)"/>
      <path d="M0 309 L0 292 L258 288 C270 288 272 282 276 272 C280 262 286 258 298 258 L540 256 L540 309 Z" fill="var(--maroon)"/>
    </svg>

    <div class="front-brand">
      <span class="brand-dot"></span>
      <span class="brand-name">BRINWOOD AUTO HUB</span>
    </div>

    <div class="person">
      <p class="person-name">DEAN MARSH</p>
      <p class="person-role">Marketing Manager</p>
    </div>

    <ul class="contact-list">
      <li>
        <svg viewBox="0 0 16 16" aria-hidden="true"><circle cx="8" cy="8" r="8" fill="var(--maroon)"/><path d="M5 4.5h2l.6 2-1 .8a5 5 0 0 0 2.1 2.1l.8-1 2 .6v2c0 .5-.5 1-1 1A7 7 0 0 1 4 5.5c0-.5.5-1 1-1z" fill="var(--white)"/></svg>
        <span>555-417-2386</span>
      </li>
      <li>
        <svg viewBox="0 0 16 16" aria-hidden="true"><circle cx="8" cy="8" r="8" fill="var(--maroon)"/><rect x="4" y="5.2" width="8" height="5.6" fill="var(--white)"/><path d="M4 5.2 8 8.4 12 5.2" fill="none" stroke="var(--maroon)" stroke-width="1"/></svg>
        <span>Dean@BrinwoodAutoHub.example</span>
      </li>
      <li>
        <svg viewBox="0 0 16 16" aria-hidden="true"><circle cx="8" cy="8" r="8" fill="var(--maroon)"/><path d="M8 3.5a3 3 0 0 1 3 3c0 2.2-3 6-3 6s-3-3.8-3-6a3 3 0 0 1 3-3z" fill="var(--white)"/><circle cx="8" cy="6.5" r="1.1" fill="var(--maroon)"/></svg>
        <span>PO Box 51820<br>Riverton, LA 70999</span>
      </li>
    </ul>

    <p class="website">www.BrinwoodAutoHub.example</p>
  </section>

</main>
</body>
</html>
```